Corvane Project Services - Flyer

Project Breif:
I need a single page A4 Capability Statement, which will be used to market our services to prospective clients, both in print and via email PDF.
It needs to look professional and should incorporate the elements I have uploaded into files, these include:
Capability Statement Text
Corvane Services Company Logo
Additional Logo’s (Tools We Use)
Glimmer Bay Pics can be cut into the page
I have included examples of capability statements as a guide to what i am looking for.
Regards
Derek
Engineering Consulting

```html
<!DOCTYPE html>
<html lang="en">
<head>
<meta charset="utf-8">
<title>Corvane Project Services – Capability Statement</title>
<link href="https://fonts.googleapis.com/css2?family=Didact+Gothic&family=Mulish:wght@400;700;800&display=swap" rel="stylesheet">
<style>
  :root{
    --blue:#3a6cb4;
    --blue-text:#3d7cc9;
    --panel-head:#87acd8;
    --panel-fill:#d8e9f5;
    --bullet:#6f9bcf;
    --grey-box:#e6e7e8;
    --ink:#222;
    --ink-soft:#555;
    --white:#fff;
  }
  *{margin:0;padding:0;box-sizing:border-box}
  html,body{width:849px;height:1200px;overflow:hidden;background:var(--white)}
  body{position:relative;font-family:"Didact Gothic",sans-serif;color:var(--ink)}
  .abs{position:absolute}

  .brand{left:60px;top:24px;width:300px;text-align:center}
  .brand-mark{width:96px;height:96px;border-radius:50%;background:var(--blue);margin:10px auto 22px}
  .brand-name{font-family:"Mulish",sans-serif;font-weight:800;color:var(--ink);font-size:21px;letter-spacing:1px;line-height:24px}

  .contact{left:438px;top:24px;width:373px;height:110px;background:var(--grey-box);border-radius:10px}
  .contact-title{position:absolute;right:22px;top:-6px;color:var(--white);font-size:28px;letter-spacing:4px;line-height:30px}
  .contact-address{position:absolute;left:26px;top:36px;width:182px;font-size:11.5px;line-height:20px;color:var(--ink-soft);font-style:normal;white-space:nowrap}
  .contact-lines{position:absolute;left:212px;top:36px;font-size:12px;line-height:20px;color:var(--ink-soft);list-style:none;white-space:nowrap}
  .contact-lines li{display:flex;align-items:center;gap:7px}
  .contact-lines svg{width:12px;height:12px;flex:none}

  .statement-bar{left:438px;top:152px;width:373px;height:44px;background:var(--blue);border-radius:9px;color:var(--white);font-size:27px;letter-spacing:3.2px;line-height:44px;text-align:center}

  .intro{left:29px;top:246px;width:373px}
  .intro .intro-lead{color:var(--blue-text);font-size:18px;line-height:25.5px;text-align:justify;margin-bottom:12px}
  .intro p{font-size:12.8px;line-height:21.6px;text-align:justify;margin-bottom:20.5px}

  .panel{background:var(--panel-fill);border-radius:7px;overflow:hidden}
  .panel-head{background:var(--panel-head);color:var(--white);font-family:"Mulish",sans-serif;font-weight:800;font-size:17.5px;letter-spacing:.5px;padding:0 16px;height:36px;line-height:36px;border-radius:7px;white-space:nowrap}
  .panel ul{list-style:none;padding:14px 0 0 0}
  .panel li{position:relative;padding-left:45px;font-size:13px;line-height:25.6px}
  .panel li::before{content:"";position:absolute;left:15px;top:9px;width:7px;height:7px;border-radius:50%;background:var(--bullet)}

  .planning{left:30px;top:638px;width:325px;height:240px}
  .risk{left:30px;top:902px;width:325px;height:213px}
  .risk .panel-head{font-weight:700;letter-spacing:.3px}
  .cost{left:438px;top:248px;width:325px;height:182px}
  .cost .panel-head{height:34px;line-height:34px}
  .cost li{padding-left:46px}

  .tools-head{left:438px;top:454px;width:325px;height:35px;line-height:35px;background:var(--panel-head);color:var(--white);font-family:"Mulish",sans-serif;font-weight:800;font-size:17.5px;letter-spacing:.5px;padding:0 16px;border-radius:7px}
  .tool{font-family:"Mulish",sans-serif;font-weight:700;font-size:15px;color:var(--blue);display:flex;align-items:center;gap:6px;white-space:nowrap}
  .tool i{display:block;width:12px;height:12px;background:var(--blue)}

  .photos{left:380px;top:560px;width:469px;height:592px}

  .footer{left:0;top:1152px;width:849px;height:48px;background:var(--blue);color:var(--white);font-size:17.5px;line-height:48px;text-align:center;letter-spacing:.4px;white-space:nowrap}
</style>
</head>
<body>

<header class="abs brand">
  <div class="brand-mark"></div>
  <div class="brand-name">CORVANE PROJECT<br>SERVICES</div>
</header>

<section class="abs contact">
  <div class="contact-title">CONTACT</div>
  <address class="contact-address">
    Corvane Project Services Limited,<br>Kilbrack, Co Cork,<br>Ireland.
  </address>
  <ul class="contact-lines">
    <li><svg viewBox="0 0 12 12"><rect x="1" y="1.5" width="10" height="7" fill="none" stroke="#3a6cb4" stroke-width="1.3"/><path d="M4 11h4M6 8.5v2.5" stroke="#3a6cb4" stroke-width="1.3"/></svg>www.corvaneservices.ie</li>
    <li><svg viewBox="0 0 12 12"><circle cx="6" cy="6" r="4.5" fill="none" stroke="#3a6cb4" stroke-width="1.3"/><circle cx="6" cy="6" r="1.8" fill="none" stroke="#3a6cb4" stroke-width="1.3"/></svg>info@corvaneservices.ie</li>
    <li><svg viewBox="0 0 12 12"><path d="M1 5c0-2 2-3 5-3s5 1 5 3l-2 1-1-1.5H4L3 6z M2.5 7h7l1 4h-9z" fill="#3a6cb4"/></svg>+353 (0)21 555 0192</li>
  </ul>
</section>

<div class="abs statement-bar">CAPABILITY STATEMENT</div>

<section class="abs intro">
  <p class="intro-lead">Corvane Project Services Ltd is a leading project control consultancy based in Co Cork Ireland.</p>
  <p>For over 20 years we have been helping our clients to deliver complex projects and programs throughout mainland Europe.</p>
  <p>We are passionate about empower organisations to achieve their objectives, on time and on budget.</p>
  <p>We are continually innovating, evolving and learning, utilize the latest industry tools and techniques to deliver real value to our clients.</p>
  <p>Our goal is to make successful project delivery more achievable and repeatable.</p>
  <p>Corvane Project Services are happy to provide</p>
</section>

<section class="abs panel planning">
  <h2 class="panel-head">Planning and Scheduling</h2>
  <ul>
    <li>Tender Planning</li>
    <li>Interactive Planning / Pull Planning</li>
    <li>EPCMV Planning &amp; Scheduling</li>
    <li>Schedule Earned Value Management</li>
    <li>Independent Schedule Quality Assessment</li>
    <li>Schedule Risk Analysis (Monte Carlo)</li>
    <li>Planning &amp; Scheduling Training</li>
  </ul>
</section>

<section class="abs panel risk">
  <h2 class="panel-head">Management of Risk (Riskway)</h2>
  <ul>
    <li>Risk Management Policies &amp; Procedures</li>
    <li>Risk Management Strategy</li>
    <li>Risk Registers</li>
    <li>Risk Improvement Planning</li>
    <li>Risk Response and Communication</li>
    <li>Risk Management Training</li>
  </ul>
</section>

<section class="abs panel cost">
  <h2 class="panel-head">Cost Control:</h2>
  <ul>
    <li>Estimating &amp; Forecasting</li>
    <li>Change Management</li>
    <li>Earned Value Analysis</li>
    <li>Progress Reporting</li>
    <li>Cost Risk Analysis</li>
  </ul>
</section>

<h2 class="abs tools-head">Our Tools:</h2>
<div class="abs tool" style="left:445px;top:524px">Tessel Planner</div>
<div class="abs tool" style="left:562px;top:524px"><i></i>Plano Project</div>
<div class="abs tool" style="left:700px;top:524px">Riskway</div>
<div class="abs tool" style="left:438px;top:582px"><i></i>Ardent Schedule</div>
<div class="abs tool" style="left:440px;top:634px;font-size:19px">Waypoint Pro</div>
<div class="abs tool" style="left:438px;top:698px;font-size:14px">Quorin Metrics</div>

<svg class="abs photos" viewBox="0 0 469 592" role="img" aria-label="Photographs cut into circles: a Gantt chart schedule printout, and hands holding a pen over project reports">
  <defs>
    <linearGradient id="sheet" x1="0" y1="0" x2="1" y2="1">
      <stop offset="0" stop-color="#eef3f8"/><stop offset="1" stop-color="#c9d6e4"/>
    </linearGradient>
    <linearGradient id="desk" x1="0" y1="0" x2="1" y2="1">
      <stop offset="0" stop-color="#9fb6cf"/><stop offset=".55" stop-color="#dfe7f0"/><stop offset="1" stop-color="#e9d2c4"/>
    </linearGradient>
  </defs>
  <circle cx="252" cy="448" r="244" fill="url(#desk)" stroke="#fff" stroke-width="6"/>
  <circle cx="345" cy="155" r="145" fill="url(#sheet)" stroke="#fff" stroke-width="6"/>
</svg>

<footer class="abs footer">Our goal is to bring reliability, consistency and repeatability to project execution and delivery.</footer>

</body>
</html>
```